2in1 Bartender & Sommelier needs a business card

I need a business card. I worked as a bartender in many places but I just finished a sommelier school and I would like a new business card. I like minimal design, natural materials and something what makes the people think :) I try to be creative in cocktail making, like little mixology, little twist on recipes... I like to travel and discover new places, cultures and of course interesting drinks and improve continously...live a little bit crazy life. And I like what I do...

Target Market(s)

restaurant/winebar managers, winemakers, other sommeliers and bartenders, people who work in food and beverage sector

Industry/Entity Type

Hospitality

Contact Information for Business Card

Rozsa Tarkany
Bartender & Sommelier
Phone: (FR) +33 6 4827 3190
(HU) +36 70 918 6352

Font styles to use
Script

Requirements
Must have
• Some sign, I am a bartender and sommelier as well.
Nice to have
• black and white maybe with 1 or 2 extra color
Should not have
• very colourful, to many things on the card

```html
<!DOCTYPE html>
<html lang="en">
<head>
<meta charset="utf-8">
<title>Rozsa Tarkany – Business Card</title>
<link rel="stylesheet" href="https://fonts.googleapis.com/css2?family=Yellowtail&family=Montserrat:wght@500&family=Open+Sans:wght@400&display=swap">
<style>
  :root {
    --backdrop: #2f3e47;
    --card-white: #ffffff;
    --card-black: #0b0203;
    --accent-orange: #f07a10;
    --ink-dark: #1a1a1a;
    --ink-light: #f4f4f4;
    --rule: #d9d9d9;
  }
  * { margin: 0; padding: 0; box-sizing: border-box; }
  html, body {
    width: 1200px;
    height: 900px;
    overflow: hidden;
    background: var(--backdrop);
  }
  .canvas {
    width: 1200px;
    height: 900px;
    display: flex;
    flex-direction: column;
    align-items: center;
    justify-content: center;
    gap: 44px;
  }
  .card {
    width: 600px;
    height: 343px;
    position: relative;
    box-shadow: 0 10px 28px rgba(0, 0, 0, 0.35);
  }
  .card--front {
    background: var(--card-white);
    display: flex;
    flex-direction: column;
    align-items: center;
    padding-top: 82px;
  }
  .card--back {
    background: var(--card-black);
    display: flex;
    flex-direction: column;
    align-items: center;
    padding-top: 26px;
  }
  .name {
    font-family: "Yellowtail", cursive;
    color: var(--accent-orange);
    line-height: 1;
    white-space: nowrap;
  }
  .card--front .name { font-size: 40px; }
  .card--back .name { font-size: 48px; }
  .role {
    white-space: nowrap;
  }
  .card--front .role {
    font-family: "Montserrat", sans-serif;
    font-weight: 500;
    font-size: 12.5px;
    letter-spacing: 0.6px;
    color: var(--ink-dark);
    margin-top: 2px;
  }
  .name-rule {
    width: 222px;
    height: 1px;
    background: var(--rule);
    margin-top: 4px;
  }
  .card--back .role {
    font-family: "Open Sans", sans-serif;
    font-size: 15px;
    letter-spacing: 0.7px;
    color: var(--ink-light);
    margin-top: 6px;
  }
  .contact-list {
    list-style: none;
    margin-top: 62px;
    text-align: center;
    font-family: "Open Sans", sans-serif;
    font-size: 17px;
    letter-spacing: 0.6px;
    line-height: 26px;
    color: var(--ink-light);
  }
</style>
</head>
<body>
  <main class="canvas">
    <section class="card card--front" aria-label="Business card front">
      <h1 class="name">Rozsa Tarkany</h1>
      <p class="role">Bartender &amp; Sommelier</p>
    </section>

    <section class="card card--back" aria-label="Business card back">
      <h2 class="name">Rozsa Tarkany</h2>
      <div class="name-rule"></div>
      <p class="role">Bartender &amp; Sommelier</p>
      <ul class="contact-list">
        <li>+36 70 918 6352</li>
        <li>+33 6 4827 3190</li>
        <li>info@your.com</li>
        <li>www.yourdomain.com</li>
        <li>yourusername</li>
      </ul>
    </section>
  </main>
</body>
</html>
```